Australian Civil Construction, Quarry & Mining Services needs a business card

We need a business card designed for our Civil Construction, Quarry & Mining Services based in the country in Australia.
Our Company Brackley Earthworks provide innovate solutions for infrastructure, agricultural and mining (aggregate, sand, roadbase) industry.
We would like our business cards to be double sided
Front of card: black background or something that resembles our business colours. (it doesn't have to be black we are open to options)
- Company name - Brackley Earthworks
- Either our logo or some sort of icon/picture that resembles our business
- Website - https://brackleyearthworks.com.au/
- We will have a number of different names, positions descriptions, phone numbers and emails on separate cards for each of our managers/directors

```html
<!DOCTYPE html>
<html lang="en">
<head>
<meta charset="utf-8">
<title>Brackley Earthworks — Business Card</title>
<link rel="stylesheet" href="https://fonts.googleapis.com/css2?family=Montserrat:wght@400;500;700;800&display=swap">
<style>
  :root {
    --stage: #2a2a2c;
    --card: #161416;
    --card-back: #1b191b;
    --orange: #e0601c;
    --white: #ffffff;
    --muted: #d9d9d9;
  }
  * { margin: 0; padding: 0; box-sizing: border-box; }
  html, body { width: 1200px; height: 900px; overflow: hidden; }
  body {
    background: var(--stage);
    font-family: "Montserrat", sans-serif;
    color: var(--white);
    position: relative;
  }
  .card {
    position: absolute;
    left: 250px;
    width: 700px;
    height: 400px;
    overflow: hidden;
    box-shadow: 0 14px 34px rgba(0,0,0,.55);
  }
  .card--front { top: 40px; background: var(--card); }
  .card--back { top: 470px; background: var(--card-back); }

  /* front */
  .brand {
    position: absolute; left: 48px; top: 52px;
    display: flex; align-items: center; gap: 14px;
  }
  .brand__mark { width: 34px; height: 34px; background: var(--orange); }
  .brand__name {
    font-weight: 800; font-size: 27px; line-height: 1.05;
    letter-spacing: 1px; text-transform: uppercase; color: var(--orange);
  }
  .divider {
    position: absolute; left: 60px; top: 196px;
    width: 580px; height: 1.5px; background: var(--orange);
  }
  .person {
    position: absolute; right: 60px; top: 122px; text-align: right;
  }
  .person__name {
    font-weight: 800; font-size: 30px; letter-spacing: .5px;
    color: var(--orange); text-transform: uppercase; line-height: 1;
  }
  .person__role {
    font-weight: 400; font-size: 16px; letter-spacing: 1px;
    text-transform: uppercase; margin-top: 6px;
  }
  .accent-bar {
    position: absolute; right: 0; top: 204px;
    width: 10px; height: 40px; background: var(--orange);
  }
  .contacts {
    position: absolute; left: 52px; top: 214px;
    list-style: none; font-size: 15px; line-height: 24px; color: var(--muted);
  }
  .contacts li { display: flex; align-items: center; gap: 8px; }
  .contacts svg { width: 13px; height: 13px; flex: none; }
  .address {
    position: absolute; right: 60px; top: 222px;
    font-size: 16px; line-height: 24px; text-align: right; color: var(--muted);
  }
  .base-band { position: absolute; left: 0; bottom: 0; width: 700px; height: 80px; }

  /* back */
  .back-texture { position: absolute; inset: 0; background: linear-gradient(135deg, #1e1c1e, #141214); }
  .back-brand {
    position: absolute; right: 52px; bottom: 52px; text-align: right;
    font-weight: 800; font-size: 44px; line-height: 1.05; letter-spacing: 2px;
    text-transform: uppercase; color: var(--orange);
  }
</style>
</head>
<body>
  <section class="card card--front" aria-label="Business card front">
    <div class="brand">
      <span class="brand__mark"></span>
      <span class="brand__name">Brackley<br>Earthworks</span>
    </div>

    <div class="person">
      <p class="person__name">Daniel Harlow</p>
      <p class="person__role">President</p>
    </div>
    <div class="accent-bar"></div>
    <div class="divider"></div>

    <ul class="contacts">
      <li>
        <svg viewBox="0 0 16 16"><path d="M4 1l3 3-2 2c1 2 3 4 5 5l2-2 3 3-2 3C7 14 2 9 1 3z" fill="var(--orange)"/></svg>
        03 5912 6640
      </li>
      <li>
        <svg viewBox="0 0 16 16"><rect x="1" y="3" width="14" height="10" fill="none" stroke="var(--orange)" stroke-width="1.5"/><path d="M1 3l7 6 7-6" fill="none" stroke="var(--orange)" stroke-width="1.5"/></svg>
        admin@brackleyearthworks.com.au
      </li>
      <li>
        <svg viewBox="0 0 16 16"><circle cx="8" cy="8" r="6.5" fill="none" stroke="var(--orange)" stroke-width="1.5"/><path d="M1.5 8h13M8 1.5c-3 3-3 10 0 13M8 1.5c3 3 3 10 0 13" fill="none" stroke="var(--orange)" stroke-width="1.2"/></svg>
        brackleyearthworks.com.au
      </li>
    </ul>

    <p class="address">42 Wattle Creek Road, Kelmora<br>Victoria 3741, Australia</p>

    <svg class="base-band" viewBox="0 0 700 80" preserveAspectRatio="none" aria-hidden="true">
      <path d="M0 36 L270 74 L0 74 Z" fill="var(--white)"/>
      <path d="M0 44 L260 80 L0 80 Z" fill="var(--orange)"/>
      <path d="M200 80 C260 78 270 40 330 40 L700 40 L700 80 Z" fill="var(--orange)"/>
    </svg>
  </section>

  <section class="card card--back" aria-label="Business card back">
    <div class="back-texture" role="img" aria-label="Subtle dark tonal background texture"></div>
    <p class="back-brand">Brackley<br>Earthworks</p>
  </section>
</body>
</html>
```